Dialysis Brochure

12 pages booklet, horizontal, 9 inches width x 6 inches high , luxury look
Updates

Landscape booklet 9 x 6

Need extra days to review

Target Market(s)

General public

Industry/Entity Type

Health Care

Colors

Designer to choose colors to be used in the design.

Requirements
Nice to have
• foil effect or similar

```html
<!DOCTYPE html>
<html lang="en">
<head>
<meta charset="utf-8">
<title>Harborline Dialysis – Brochure Spreads</title>
<link href="https://fonts.googleapis.com/css2?family=Montserrat:wght@400;500;600;700;800&display=swap" rel="stylesheet">
<style>
:root{
  --bg:#c4e3e4;
  --ink:#1d1a26;
  --ink-soft:#2a2635;
  --pink:#d6336c;
  --blue:#1f9fd8;
  --white:#f3f3f6;
  --muted:#b9b6c6;
  --photo-a:#dfe3e8;
  --photo-b:#a9b0ba;
}
*{box-sizing:border-box;margin:0;padding:0}
html,body{width:1200px;height:4000px;overflow:hidden}
body{background:var(--bg);font-family:'Montserrat',sans-serif;color:var(--white);position:relative}
.spread{position:absolute;left:40px;width:1120px;height:373px;background:var(--ink);display:flex;box-shadow:0 14px 30px rgba(0,40,50,.25)}
.page{position:relative;width:560px;height:373px;overflow:hidden}
.page + .page{border-left:1px solid rgba(0,0,0,.35)}
.photo{position:absolute;background:linear-gradient(135deg,var(--photo-a),var(--photo-b))}
.photo.warm{background:linear-gradient(135deg,#e9e4dc,#a79d92)}
.page-no{position:absolute;bottom:14px;right:14px;background:var(--blue);color:#fff;font-size:10px;font-weight:600;padding:6px 12px;letter-spacing:.5px}
.heading{color:var(--blue);font-weight:700;font-size:12px;letter-spacing:1px;text-transform:uppercase}
.list{list-style:none;font-size:10.5px;line-height:1.35}
.list li{position:relative;padding-left:20px;margin-top:8px}
.list li::before{content:"»";position:absolute;left:0;color:var(--pink);font-weight:700}
.list.small{font-size:8.5px}
.list.small li{margin-top:5px}
.brand{display:flex;align-items:center;gap:8px;font-weight:700;font-size:12px;color:var(--white)}
.brand .dot{width:12px;height:12px;border-radius:50%;background:var(--pink)}
.contact{font-size:8px;line-height:1.7;color:var(--muted)}
.pill{height:26px;display:flex;align-items:center;justify-content:center;font-size:10px;font-weight:700;color:#fff}
.pill.pink{background:var(--pink)}.pill.blue{background:var(--blue)}
.pill-note{font-size:10px;text-align:center;background:var(--ink-soft);padding:5px 0;margin-bottom:10px}
table.quality{border-collapse:collapse;font-size:7.5px;width:100%}
.quality th{padding:5px;color:#fff;font-weight:600}
.quality td{padding:4px 5px;text-align:center;background:#f1f1f4;color:#333;border:1px solid #cfcfd6}
.quality td.label{background:var(--blue);color:#fff;text-align:left;border-color:#4db4e2}
.stat{display:flex;gap:16px;align-items:flex-start;margin-bottom:22px}
.stat-icon{width:50px;height:50px;background:var(--pink);flex:none;display:flex;align-items:center;justify-content:center}
.stat-title{color:var(--pink);font-size:10px;font-weight:700;text-transform:uppercase;line-height:1.1}
.stat-text{font-size:9px;line-height:1.4;margin-top:3px}
</style>
</head>
<body>

<section class="spread" style="top:252px">
  <div class="page back-cover">
    <div class="brand" style="position:absolute;left:40px;bottom:50px"><span class="dot"></span>Harborline Dialysis</div>
    <div class="photo" role="img" aria-label="Street map showing the center location" style="left:150px;top:170px;width:120px;height:70px;background:linear-gradient(135deg,#eef1f4,#c9d4dc)"></div>
    <div class="contact" style="position:absolute;left:150px;top:252px">
      Harborline Kidney Center<br>
      2400 Harbor Avenue, Bayview, NY 10000<br>
      <span style="color:var(--blue)">●</span> 1 (555) 010-2400 &nbsp; <span style="color:var(--blue)">●</span> info@harborline.example
    </div>
    <div style="position:absolute;left:330px;top:110px;width:190px">
      <div style="background:var(--blue);color:#fff;font-size:9px;font-weight:700;padding:4px 8px;display:inline-block">DIRECTIONS</div>
      <p style="font-size:7.5px;line-height:1.5;margin-top:8px;color:var(--muted)">Our center sits near the marina with easy access by car, bus and subway. Free parking is available on site.</p>
      <p style="font-size:7.5px;line-height:1.5;margin-top:6px;color:var(--muted)">By subway: take the line to Bayview station and walk two blocks south. By bus: stops at the corner of Harbor Avenue, steps from our entrance.</p>
    </div>
  </div>
  <div class="page front-cover">
    <svg width="200" height="200" style="position:absolute;left:40px;top:86px" viewBox="0 0 200 200">
      <circle cx="100" cy="100" r="96" fill="none" stroke="var(--pink)" stroke-width="5"/>
      <path d="M100 4 A96 96 0 0 1 196 100" fill="none" stroke="var(--blue)" stroke-width="5"/>
    </svg>
    <div class="photo" role="img" aria-label="Nurse caring for a patient in the treatment room" style="left:50px;top:96px;width:180px;height:180px;border-radius:50%"></div>
    <div style="position:absolute;left:215px;top:120px;width:60px;height:60px;border-radius:50%;background:var(--pink);opacity:.35"></div>
    <div class="brand" style="position:absolute;right:40px;top:34px"><span class="dot"></span>Harborline Dialysis</div>
    <div style="position:absolute;left:290px;top:170px">
      <div style="font-size:13px;font-weight:600;letter-spacing:1px">THIS CENTER IS A</div>
      <div style="font-size:22px;font-weight:800;color:var(--blue);letter-spacing:1px">GIFT OF LIFE</div>
    </div>
  </div>
</section>

<section class="spread" style="top:877px">
  <div class="page">
    <div style="position:absolute;left:30px;top:140px;width:8px;height:110px;background:var(--pink)"></div>
    <div style="position:absolute;left:52px;top:135px;width:150px;font-size:12px;line-height:1.35">
      <p>Harborline Dialysis is a 62-Station state-of-the-art facility.</p>
      <p style="margin-top:14px">The Largest Independent Dialysis Center in The United States.</p>
    </div>
    <div class="photo" role="img" aria-label="Exterior entrance of the dialysis center" style="left:220px;top:20px;width:120px;height:160px;background:linear-gradient(135deg,#c9d2c2,#7f8a7c)"></div>
    <div class="photo" role="img" aria-label="Reception area interior" style="left:220px;top:190px;width:120px;height:165px"></div>
    <div class="photo" role="img" aria-label="Treatment floor with dialysis chairs" style="left:350px;top:20px;width:210px;height:335px"></div>
    <div class="page-no">PAGE 2</div>
  </div>
  <div class="page">
    <div class="photo" role="img" aria-label="Bright open treatment hall with staff" style="left:0;top:0;width:560px;height:373px"></div>
    <div class="page-no">PAGE 3</div>
  </div>
</section>

<section class="spread" style="top:1502px">
  <div class="page">
    <div class="photo" role="img" aria-label="Dialysis chairs and machines" style="left:0;top:0;width:250px;height:373px"></div>
    <div style="position:absolute;left:270px;top:55px;width:250px">
      <div class="pill pink">Regular shifts</div>
      <div class="pill-note">Monday/Wednesday/Friday<br>or<br>Tuesday/Thursday/Saturday</div>
      <div class="pill blue">Early Morning shifts</div>
      <div class="pill-note">As early as 5AM</div>
      <div class="pill pink">Late Afternoon Shifts</div>
      <div class="pill-note">After 5PM</div>
    </div>
    <div class="page-no">PAGE 4</div>
  </div>
  <div class="page">
    <div class="photo" role="img" aria-label="Entrance corridor with glass door" style="left:0;top:0;width:280px;height:373px"></div>
    <div style="position:absolute;left:300px;top:60px;width:230px">
      <div class="heading">Doctor's Services</div>
      <ul class="list">
        <li>Full-time Nephrology staff physician on premises</li>
        <li>11 Board Certified Nephrologists</li>
        <li>YOU MAY KEEP YOUR CURRENT NEPHROLOGIST when you transfer to our Center</li>
      </ul>
    </div>
    <div class="page-no">PAGE 5</div>
  </div>
</section>

<section class="spread" style="top:2127px">
  <div class="page">
    <div class="photo warm" role="img" aria-label="Treatment chairs beside wood panelling" style="left:0;top:0;width:250px;height:373px"></div>
    <div style="position:absolute;left:270px;top:70px;width:260px">
      <div class="heading">Accomodations</div>
      <ul class="list">
        <li>All Dialysis chairs are with Heat and Massage functions</li>
        <li>Large 19" Flat screen TV with Cable TV for each station</li>
        <li>Individual tablets are available for Patient's use during treatment</li>
        <li>Wi-Fi/High-Speed Internet</li>
        <li>Multilingual Staff. Assistance with Spanish, Russian, Chinese and other languages.</li>
      </ul>
    </div>
    <div class="page-no">PAGE 6</div>
  </div>
  <div class="page">
    <div class="photo" role="img" aria-label="Glass-walled lounge" style="left:0;top:0;width:330px;height:186px"></div>
    <div style="position:absolute;left:330px;top:0;width:230px;height:186px;background:var(--blue);padding:40px 24px;font-size:12px;font-weight:800;line-height:1.2">SEPARATE EXTENDED-STAY LOUNGE/WAITING ROOM FOR RELATIVES AND CAREGIVERS</div>
    <div style="position:absolute;left:0;top:186px;width:230px;height:187px;background:var(--pink);padding:40px 30px;font-size:12px;font-weight:800;line-height:1.2">OUTDOOR TERRACE WITH VIEW OF THE MARINA</div>
    <div class="photo" role="img" aria-label="Waiting lounge seating" style="left:230px;top:186px;width:330px;height:187px"></div>
    <div class="page-no">PAGE 7</div>
  </div>
</section>

<section class="spread" style="top:2752px">
  <div class="page">
    <div style="position:absolute;left:40px;top:60px;width:460px">
      <div class="stat">
        <div class="stat-icon"><svg width="28" height="28" viewBox="0 0 28 28" fill="none" stroke="#fff" stroke-width="2"><path d="M2 20h24M5 20v-8h18v8M9 12V8h10v4"/></svg></div>
        <div><div class="stat-title">Patient<br>Survival Rate</div><div class="stat-text">Harborline had the Lowest Mortality Rate (higher survival) in New York State for 2011-2017 years - 11.7 (per 100 patients)</div></div>
      </div>
      <div class="stat">
        <div class="stat-icon"><svg width="28" height="28" viewBox="0 0 28 28" fill="none" stroke="#fff" stroke-width="2"><path d="M14 24s-9-6-9-12a5 5 0 0 1 9-3 5 5 0 0 1 9 3c0 6-9 12-9 12z"/></svg></div>
        <div><div class="stat-title">CareScore<br>Rating</div><div class="stat-text">Harborline received 5-Star rating 9 times out of the last 10 years. Only 15% of Dialysis Centers in the United States receive 5-Star rating in any particular year</div></div>
      </div>
      <div class="stat">
        <div class="stat-icon"><svg width="28" height="28" viewBox="0 0 28 28" fill="none" stroke="#fff" stroke-width="2"><path d="M14 3l9 4v7c0 6-4 9-9 11-5-2-9-5-9-11V7z"/><path d="M10 14l3 3 5-6"/></svg></div>
        <div><div class="stat-title">Patient<br>Safety Program</div><div class="stat-text">Gold Shield Award - 2016, 2017, 2018. Every single year starting 2016 when this program was established</div></div>
      </div>
    </div>
    <div class="page-no">PAGE 8</div>
  </div>
  <div class="page">
    <div style="position:absolute;left:30px;top:30px;width:500px">
      <table class="quality">
        <tr><th style="background:var(--blue);text-align:left">Quality Data</th><th style="background:var(--blue)">5-Star</th><th style="background:var(--pink)">Harborline</th><th style="background:var(--pink)">Average U.S.</th></tr>
        <tr><td class="label">Quality of Care</td><td>72.7</td><td>Better than expected</td><td>71.4</td></tr>
        <tr><td class="label">Infection Rate</td><td>0.24</td><td>Better than expected</td><td>1.05</td></tr>
        <tr><td class="label">Readmission Rate</td><td>0.8</td><td>As expected</td><td>29.2</td></tr>
        <tr><td class="label">Waste Removal</td><td>96.3%</td><td>As expected</td><td>95.9%</td></tr>
        <tr><td class="label">Hospitalizations</td><td>161.2</td><td>Better than expected</td><td>163.2</td></tr>
      </table>
    </div>
    <div style="position:absolute;left:30px;top:230px;width:170px;color:var(--pink);font-size:8.5px;font-weight:600;line-height:1.4;text-transform:uppercase">Over the last ten years we have consistently outperformed other dialysis centers in the area.</div>
    <ul class="list small" style="position:absolute;left:220px;top:222px;width:300px">
      <li>Higher survival rate for our patients</li>
      <li>The lower infection incidents rate</li>
      <li>The most efficiency of removal waste from blood</li>
      <li>The higher patient satisfaction rate</li>
    </ul>
    <div class="page-no">PAGE 9</div>
  </div>
</section>

<section class="spread" style="top:3377px">
  <div class="page">
    <div class="photo" role="img" aria-label="Reception desk with marble wall" style="left:0;top:0;width:250px;height:373px;background:linear-gradient(135deg,#f1f1f1,#b5b5b8)"></div>
    <div style="position:absolute;left:270px;top:50px;width:260px">
      <div class="heading" style="color:var(--pink)">Kidney Transplant Program</div>
      <p style="font-size:8.5px;line-height:1.4;margin-top:8px">Every patient of Harborline who is interested in kidney transplant will be referred to a transplant center affiliated with the following hospitals:</p>
      <ul class="list small">
        <li>Westbridge University Medical Center</li>
        <li>Northfield Medical Center</li>
        <li>Eastgate Medical Center</li>
        <li>Summit Hill Medical Center</li>
        <li>Riverside Medical Center/Alder College of Medicine</li>
      </ul>
    </div>
    <div class="page-no">PAGE 10</div>
  </div>
  <div class="page">
    <div class="photo warm" role="img" aria-label="Lounge with round table and chairs" style="left:0;top:0;width:250px;height:373px"></div>
    <div style="position:absolute;left:270px;top:50px;width:260px">
      <div class="heading" style="color:var(--pink)">Social Worker Services</div>
      <ul class="list small">
        <li>Assisting with applying or obtaining insurance coverage</li>
        <li>Locate and access community resources</li>
        <li>Apply and obtain financial assistance and aid</li>
        <li>Arrange transportation</li>
        <li>Home care services</li>
        <li>Physical, Occupational and Speech therapies</li>
        <li>Coordinate dialysis and work schedule, Vocational Rehabilitation</li>
        <li>Arrange Dialysis while you travel</li>
        <li>Professional counseling to patients and family</li>
      </ul>
    </div>
    <div class="page-no">PAGE 11</div>
  </div>
</section>

</body>
</html>
```